Modern Irish Pub. We need to find "our look" for new bar.

We have a logo, color scheme and feel of what we want but we need someone to work with to create flyer designs, menu, website and social content.

Young vibrant mixed with traditional Irish. Think neon & sexy mixed with wood and traditional Irish.

Looking for examples of social media posts and flyers. We can then hire for more work! We need to find “our look”.

Target Market(s)

21-40 year olds

Industry/Entity Type

Bar and Restaurant.

Colors
EB3D1F
EC4F4E
F09395
F8D3D4
FCEDEE

Requirements
Must have
• Our logo.
Nice to have
• Young mixed with traditional. Sexy l, vibrant and fun.
Should not have
• Cartoon like child like look and feel.

```html
<!DOCTYPE html>
<html lang="en">
<head>
<meta charset="utf-8">
<title>Crimson Clover – Social Posts &amp; Happy Hour Flyer</title>
<link rel="stylesheet" href="https://fonts.googleapis.com/css2?family=Bebas+Neue&family=Oswald:wght@400;500&family=Dancing+Script:wght@500&family=Montserrat:wght@400&display=swap">
<style>
  :root {
    --red: #EB3D1F;
    --red-soft: #EC4F4E;
    --pink: #F09395;
    --blush: #F8D3D4;
    --mist: #FCEDEE;
    --white: #ffffff;
    --ink: #111111;
    --page: #ffffff;
  }
  * { margin: 0; padding: 0; box-sizing: border-box; }
  html, body { width: 1200px; height: 1200px; overflow: hidden; background: var(--page); }
  .board { position: relative; width: 1200px; height: 1200px; }

  .board-note {
    position: absolute;
    font-family: "Montserrat", sans-serif;
    font-size: 13px;
    letter-spacing: 1.2px;
    color: var(--ink);
  }
  .note-posts { left: 620px; top: 44px; }
  .note-flyer { left: 1012px; top: 205px; }

  .panel { position: absolute; overflow: hidden; }
  .post { width: 547px; height: 548px; left: 51px; }
  .post-laughs { top: 46px; }
  .post-stories { top: 612px; }
  .flyer { left: 620px; top: 249px; width: 537px; height: 912px; }

  .photo { position: absolute; inset: 0; }
  .post-laughs .photo {
    background:
      linear-gradient(180deg, rgba(0,0,0,0) 45%, rgba(20,20,22,.55) 75%, rgba(15,15,17,.85) 100%),
      radial-gradient(ellipse 60% 45% at 75% 35%, rgba(190,40,30,.55), rgba(190,40,30,0) 70%),
      radial-gradient(ellipse 50% 40% at 35% 45%, rgba(120,30,25,.45), rgba(120,30,25,0) 70%),
      linear-gradient(180deg, #8f8f8f 0%, #a8a8a8 40%, #7a7a7a 70%, #4a4a4a 100%);
  }
  .post-stories .photo {
    background:
      linear-gradient(180deg, rgba(0,0,0,0) 45%, rgba(20,20,22,.6) 75%, rgba(15,15,17,.9) 100%),
      radial-gradient(ellipse 45% 40% at 85% 35%, rgba(200,45,35,.5), rgba(200,45,35,0) 70%),
      radial-gradient(ellipse 55% 45% at 55% 50%, rgba(210,210,210,.35), rgba(210,210,210,0) 70%),
      linear-gradient(180deg, #4a4a4a 0%, #7d7d7d 40%, #5a5a5a 70%, #2a2a2a 100%);
  }
  .flyer .photo {
    background:
      radial-gradient(ellipse 40% 35% at 18% 78%, rgba(252,237,238,.95), rgba(248,211,212,.6) 45%, rgba(248,211,212,0) 80%),
      radial-gradient(ellipse 55% 45% at 50% 75%, rgba(235,61,31,.95), rgba(235,61,31,.55) 50%, rgba(235,61,31,0) 85%),
      linear-gradient(180deg, #0c0c0c 0%, #161616 35%, #2a1410 60%, #3a1a14 85%, #1a1a1a 100%);
  }

  .brand-mark {
    position: absolute;
    display: flex;
    align-items: center;
    gap: 10px;
    font-family: "Oswald", sans-serif;
    font-weight: 500;
    color: var(--white);
    letter-spacing: 1px;
    line-height: 1;
  }
  .brand-mark .dot { width: 16px; height: 16px; border-radius: 50%; background: var(--red); flex: none; }
  .post .brand-mark { left: 40px; top: 100px; font-size: 30px; }
  .flyer .brand-mark { left: 0; right: 0; justify-content: center; top: 105px; font-size: 38px; }

  .rule {
    position: absolute;
    width: 8px;
    border-left: 2px solid var(--red);
    border-right: 2px solid var(--red);
    bottom: 0;
  }
  .post .rule { left: 22px; top: 366px; }
  .flyer .rule { left: 18px; top: 757px; }

  .caption { position: absolute; left: 40px; right: 10px; top: 366px; color: var(--white); }
  .caption .lead {
    font-family: "Oswald", sans-serif;
    font-weight: 400;
    font-size: 16px;
    letter-spacing: 2px;
    line-height: 1.2;
    white-space: nowrap;
  }
  .caption .headline {
    margin-top: 6px;
    font-family: "Bebas Neue", sans-serif;
    font-size: 38px;
    line-height: 1.05;
    white-space: nowrap;
  }
  .caption .aside {
    margin-top: 6px;
    padding-right: 36px;
    font-family: "Dancing Script", cursive;
    font-weight: 500;
    font-size: 21px;
    color: var(--red);
    text-align: right;
    white-space: nowrap;
  }

  .happy-title {
    position: absolute; left: 0; right: 0; top: 268px;
    text-align: center;
    font-family: "Oswald", sans-serif;
    font-weight: 400;
    font-size: 78px;
    letter-spacing: 9px;
    color: var(--white);
    line-height: 1;
  }
  .happy-day {
    position: absolute; right: 62px; top: 352px;
    font-family: "Dancing Script", cursive;
    font-weight: 500;
    font-size: 56px;
    color: var(--white);
    line-height: 1;
  }
  .happy-time {
    position: absolute; right: 60px; top: 576px;
    font-family: "Oswald", sans-serif;
    font-weight: 400;
    font-size: 48px;
    letter-spacing: 4px;
    color: var(--white);
    line-height: 1;
  }

  .contact {
    position: absolute; left: 38px; top: 762px;
    font-family: "Oswald", sans-serif;
    font-weight: 500;
    font-size: 17px;
    letter-spacing: 2px;
    color: var(--ink);
  }
  .contact-row { display: flex; align-items: flex-start; gap: 12px; }
  .contact-row + .contact-row { margin-top: 22px; align-items: center; }
  .contact svg { flex: none; margin-top: 2px; }
  .contact .social-dot { width: 14px; height: 14px; border-radius: 50%; background: var(--ink); margin: 0 2px; flex: none; }
  .contact address { font-style: normal; line-height: 1.55; }
</style>
</head>
<body>
<main class="board">
  <p class="board-note note-posts">&lt;&lt; 2 x &nbsp;social media posts</p>
  <p class="board-note note-flyer">&or;&nbsp; happy hour flyer</p>

  <section class="panel post post-laughs">
    <div class="photo" role="img" aria-label="Black and white photo of two laughing friends in red top hats and party glasses, red accents"></div>
    <div class="brand-mark"><span class="dot"></span>CRIMSON CLOVER</div>
    <div class="rule"></div>
    <div class="caption">
      <p class="lead">YOU COULD SAY “CHEEEEEEESE”...</p>
      <p class="headline">OR YOU COULD DROP BY<br>FOR SOME GENUINE LAUGHS.</p>
      <p class="aside">...and beer. Cause that’s always cheerful.</p>
    </div>
  </section>

  <section class="panel post post-stories">
    <div class="photo" role="img" aria-label="Black and white photo of friends toasting pints at the bar, one in a red hat"></div>
    <div class="brand-mark"><span class="dot"></span>CRIMSON CLOVER</div>
    <div class="rule"></div>
    <div class="caption">
      <p class="lead">YOU COULD AVOID TEMPORARY HANGOVERS...</p>
      <p class="headline">OR YOU COULD DROP BY<br>FOR DRUNK STORIES THAT ARE FOREVER.</p>
      <p class="aside">...and new friends. Cause they’re the best.</p>
    </div>
  </section>

  <section class="panel flyer">
    <div class="photo" role="img" aria-label="Dark photo of a bartender pouring beer from taps, glowing red and white light"></div>
    <div class="brand-mark"><span class="dot"></span>CRIMSON CLOVER</div>
    <h1 class="happy-title">HAPPY HOUR</h1>
    <p class="happy-day">every Wednesday</p>
    <p class="happy-time">4PM-5PM</p>
    <div class="rule"></div>
    <div class="contact">
      <div class="contact-row">
        <svg width="18" height="26" viewBox="0 0 18 26" aria-hidden="true"><path d="M9 1a8 8 0 0 0-8 8c0 6 8 16 8 16s8-10 8-16a8 8 0 0 0-8-8z" fill="#111"/><circle cx="9" cy="9" r="3.2" fill="#fcedee"/></svg>
        <address>18 Harbor Lane<br>Dayton, Ohio</address>
      </div>
      <div class="contact-row">
        <span class="social-dot"></span>
        <span>@CrimsonClover</span>
      </div>
    </div>
  </section>
</main>
</body>
</html>
```